Velvet Harbor small batch hot sauce label project

I am launching a line of small batch sauces (hot sauces, bbq sauces) and I need a label for my bottles. I have a logo that I like, I'm not completely married to it but It is a good logo. I would like the name of my business and the name of the sauce on the label. Something fun, edgy that would make you want to pick it up off the shelf.

Target Market(s)

Milennials, food bloggers, stay at home moms who want to amp up their dishes with a really good sauce

Industry/Entity Type

Cooking

Requirements
Must have
• I am open to interpretation
Nice to have
• Maybe a bomb cloud since I want to go in the sauce bomb direction.

```html
<!DOCTYPE html>
<html lang="en">
<head>
<meta charset="utf-8">
<title>Velvet Harbor – Garlic &amp; Harissa Hot Sauce Label</title>
<link rel="stylesheet" href="https://fonts.googleapis.com/css2?family=Lilita+One&display=swap">
<style>
  :root {
    --sauce-red: #c32f33;
    --sauce-red-light: #d6565a;
    --peach: #fde3d3;
    --peach-soft: #fff6f0;
    --paper: #ffffff;
    --cream: #fdf0d8;
    --orange: #f39a3a;
    --orange-deep: #e9782a;
    --char: #352a29;
    --char-edge: #5a2a22;
    --ink: #3a3232;
  }
  html, body {
    margin: 0;
    padding: 0;
    width: 1200px;
    height: 2490px;
    overflow: hidden;
    background: var(--paper);
  }
  .canvas {
    position: relative;
    width: 1200px;
    height: 2490px;
    background: var(--paper);
    font-family: "Lilita One", sans-serif;
  }

  /* Neck label */
  .neck-label {
    position: absolute;
    left: 136px;
    top: 0;
    width: 928px;
    height: 351px;
    overflow: hidden;
  }
  .neck-label .pattern-field {
    position: absolute;
    inset: 0 0 87px 0;
    background: linear-gradient(160deg, var(--peach) 0%, var(--peach-soft) 55%, var(--peach) 100%);
  }
  .neck-label .brand {
    position: absolute;
    left: 0;
    right: 0;
    top: 100px;
    display: flex;
    align-items: center;
    justify-content: center;
    gap: 22px;
  }
  .neck-label .brand-name {
    font-size: 58px;
    color: var(--ink);
    letter-spacing: 2px;
  }
  .neck-label .red-band {
    position: absolute;
    left: 0;
    right: 0;
    bottom: 0;
    height: 87px;
    background: var(--sauce-red);
  }

  .brand-dot {
    width: 40px;
    height: 40px;
    border-radius: 50%;
    background: var(--ink);
  }

  /* Main body label */
  .body-label {
    position: absolute;
    left: 0;
    top: 574px;
    width: 1200px;
    height: 1887px;
    overflow: hidden;
  }
  .body-label .pattern-field {
    position: absolute;
    left: 0;
    right: 0;
    top: 382px;
    bottom: 152px;
    background: linear-gradient(165deg, var(--peach) 0%, var(--peach-soft) 40%, var(--peach) 75%, var(--peach-soft) 100%);
  }
  .body-label .top-band {
    position: absolute;
    left: 0;
    right: 0;
    top: 0;
    height: 382px;
    background: linear-gradient(180deg, var(--sauce-red) 0%, var(--sauce-red) 70%, var(--sauce-red-light) 100%);
  }
  .body-label .bottom-band {
    position: absolute;
    left: 0;
    right: 0;
    bottom: 0;
    height: 152px;
    background: var(--sauce-red);
  }

  .flavour {
    position: absolute;
    left: 0;
    right: 0;
    top: 80px;
    margin: 0;
    text-align: center;
    font-size: 96px;
    font-weight: 400;
    color: var(--cream);
    letter-spacing: 1px;
    text-shadow: 5px 5px 0 var(--char);
  }
  .heat-word {
    position: absolute;
    left: 0;
    right: 0;
    top: 190px;
    margin: 0;
    text-align: center;
    font-size: 250px;
    line-height: 1;
    font-weight: 400;
    color: #fde9d6;
    letter-spacing: 4px;
    -webkit-text-stroke: 8px var(--orange);
    paint-order: stroke fill;
    text-shadow: 10px 8px 0 var(--char);
  }

  .sauce-banner {
    position: absolute;
    left: 356px;
    top: 437px;
    width: 464px;
    height: 149px;
  }
  .sauce-banner svg {
    position: absolute;
    inset: 0;
  }
  .sauce-banner .label-text {
    position: absolute;
    inset: 0;
    display: flex;
    align-items: center;
    justify-content: center;
    font-size: 74px;
    color: var(--orange);
    letter-spacing: 2px;
    padding-bottom: 8px;
  }

  .bomb-cloud {
    position: absolute;
    left: 244px;
    top: 586px;
    width: 603px;
    height: 825px;
    border-radius: 48% 48% 20% 20% / 40% 40% 14% 14%;
    background: radial-gradient(ellipse at 50% 25%, var(--cream) 0%, #f7d9a8 35%, var(--orange) 65%, #8a3e24 100%);
  }

  .body-label .brand {
    position: absolute;
    left: 0;
    right: 0;
    top: 1455px;
    display: flex;
    align-items: center;
    justify-content: center;
    gap: 22px;
  }
  .body-label .brand-name {
    font-size: 62px;
    color: var(--ink);
    letter-spacing: 2px;
  }

  .heat-badge {
    position: absolute;
    left: 456px;
    top: 1594px;
    width: 248px;
    height: 248px;
  }
</style>
</head>
<body>
<main class="canvas">

  <section class="neck-label" aria-label="Neck label">
    <div class="pattern-field" role="img" aria-label="Soft peach zigzag stripe pattern"></div>
    <div class="brand">
      <span class="brand-dot" aria-hidden="true"></span>
      <span class="brand-name">Velvet Harbor</span>
    </div>
    <div class="red-band"></div>
  </section>

  <section class="body-label" aria-label="Main bottle label">
    <div class="top-band"></div>
    <div class="pattern-field" role="img" aria-label="Soft peach zigzag stripe pattern"></div>
    <div class="bottom-band"></div>

    <h1 class="flavour">GARLIC &amp; HARISSA</h1>
    <h2 class="heat-word">HOT</h2>

    <div class="sauce-banner">
      <svg viewBox="0 0 464 149" width="464" height="149" aria-hidden="true">
        <polygon points="0,0 464,18 440,149 22,135" fill="var(--char-edge)"/>
        <polygon points="10,8 456,24 432,140 30,128" fill="var(--char)"/>
      </svg>
      <span class="label-text">SAUCE</span>
    </div>

    <div class="bomb-cloud" role="img" aria-label="Illustration of an exploding mushroom cloud, the sauce bomb"></div>

    <div class="brand">
      <span class="brand-dot" aria-hidden="true"></span>
      <span class="brand-name">Velvet Harbor</span>
    </div>

    <svg class="heat-badge" viewBox="0 0 248 248" width="248" height="248" aria-label="Heat level badge" role="img">
      <circle cx="124" cy="124" r="120" fill="var(--char)"/>
      <circle cx="124" cy="124" r="100" fill="var(--sauce-red)"/>
      <circle cx="124" cy="124" r="84" fill="var(--char)"/>
    </svg>
  </section>

</main>
</body>
</html>
```